MOLVT Study flyer

I need help designing a flyer for a research study that will include brain imaging in adolescents. The info is in the attached document. The study is called the Marrowby Orchard Lantern Vesper Trail (MOLVT) study. Ideally this would be returned as a document that I can edit in the future as we will have several new recruitment phases (different age groups, etc. I also would love to have a logo designed as part of this project, but I recognize that might be a separate design request.

```html
<!DOCTYPE html>
<html lang="en">
<head>
<meta charset="utf-8">
<title>MOLVT Study Flyer</title>
<link rel="stylesheet" href="https://fonts.googleapis.com/css2?family=Oswald:wght@500&family=Montserrat:wght@800&family=Raleway:wght@400;500;700;800&display=swap">
<style>
  :root {
    --navy: #172d4f;
    --orange: #e99b15;
    --white: #ffffff;
    --ink: #1d2f52;
    --backdrop: #d6d7d9;
    --photo-dark: #4a4744;
    --photo-mid: #8a8784;
    --photo-light: #c9c8c6;
    --rule: #e4e4e4;
  }
  * { box-sizing: border-box; margin: 0; padding: 0; }
  html, body { width: 1200px; height: 2400px; overflow: hidden; }
  body { background: var(--backdrop); position: relative; font-family: "Raleway", Arial, sans-serif; }

  .flyer {
    position: absolute; left: 0; top: 351px;
    width: 1200px; height: 1697px;
    background: var(--white); overflow: hidden;
  }

  .hero {
    position: absolute; left: 0; top: 0; width: 1200px; height: 808px;
    background:
      radial-gradient(ellipse at 55% 55%, var(--photo-mid) 0%, transparent 55%),
      linear-gradient(180deg, var(--photo-light) 0%, #a9a7a4 45%, var(--photo-dark) 100%);
  }
  .hero-text {
    position: absolute; left: 0; right: 0; top: 568px; text-align: center; color: var(--white);
    text-shadow: 0 2px 6px rgba(0,0,0,.35);
  }
  .hero-kicker { font-family: "Oswald", "Arial Narrow", sans-serif; font-weight: 500; font-size: 42px; letter-spacing: .5px; }
  .hero-title { font-family: "Montserrat", Arial, sans-serif; font-weight: 800; font-size: 55px; line-height: 74px; margin-top: 4px; }

  .intro {
    position: absolute; left: 60px; right: 60px; top: 853px; text-align: center;
    color: var(--ink); font-size: 22px; line-height: 29px;
  }

  .participation {
    position: absolute; left: 91px; top: 939px; width: 538px; height: 476px;
    background: var(--orange); border-radius: 52px; padding: 44px 38px 0 40px; color: var(--white);
  }
  .participation h2 { font-family: "Raleway", sans-serif; font-weight: 800; font-size: 36px; line-height: 44px; text-transform: uppercase; margin-bottom: 26px; }
  .participation ul { list-style: none; }
  .participation li { display: flex; gap: 18px; font-size: 18px; line-height: 23px; margin-bottom: 26px; }
  .participation li svg { flex: none; margin-top: 2px; }

  .eligibility { position: absolute; left: 662px; top: 957px; width: 440px; color: var(--ink); }
  .eligibility h2 { font-weight: 800; font-size: 37px; line-height: 46px; text-transform: uppercase; margin-bottom: 18px; }
  .criterion { display: flex; align-items: flex-start; gap: 30px; padding: 6px 0 28px; border-bottom: 1px solid var(--rule); width: 360px; margin-bottom: 22px; font-size: 22px; line-height: 28px; }
  .criterion:last-child { border-bottom: none; }
  .criterion svg { flex: none; }

  .cta { position: absolute; left: 103px; top: 1441px; color: var(--ink); font-weight: 800; font-size: 28px; line-height: 36px; text-transform: uppercase; }

  .footer-band { position: absolute; left: 0; bottom: 0; width: 1200px; height: 170px; }
  .email {
    position: absolute; left: 115px; top: 1557px; height: 58px; padding: 0 20px;
    background: var(--orange); border-radius: 29px; color: var(--white);
    font-weight: 700; font-size: 34px; line-height: 58px;
  }
  .study-name {
    position: absolute; left: 633px; top: 1530px; color: var(--white);
    font-family: "Raleway", sans-serif; font-weight: 500; font-size: 100px; letter-spacing: 4px; line-height: 120px;
  }
</style>
</head>
<body>
<main class="flyer">
  <div class="hero" role="img" aria-label="Photo of a teenager in a grey hoodie holding their head, with hand-drawn speech bubbles of scribbles, a sad face and question marks above"></div>
  <div class="hero-text">
    <p class="hero-kicker">ARE YOU THE PARENT OF A CHILD AGE 10-17?</p>
    <h1 class="hero-title">DO THEY WORRY OR OVERTHINK<br>NEGATIVE EMOTIONS?</h1>
  </div>

  <p class="intro">Halvern University researchers are seeking girls age 10-17 for a study about brain activity in emotions and decision-making and how they relate to puberty, anxiety and depression.</p>

  <section class="participation">
    <h2>Study participation<br>involves</h2>
    <ul>
      <li><svg width="22" height="22" viewBox="0 0 22 22"><circle cx="11" cy="11" r="9" fill="none" stroke="#1d2f52" stroke-width="2"/><path d="M6.5 11.5l3 3 6-6" fill="none" stroke="#1d2f52" stroke-width="2"/></svg><span>One one-hour interview (online or in-person) where your child will discuss their thoughts</span></li>
      <li><svg width="22" height="22" viewBox="0 0 22 22"><circle cx="11" cy="11" r="9" fill="none" stroke="#1d2f52" stroke-width="2"/><path d="M6.5 11.5l3 3 6-6" fill="none" stroke="#1d2f52" stroke-width="2"/></svg><span>Online questionnaires (parent and child)</span></li>
      <li><svg width="22" height="22" viewBox="0 0 22 22"><circle cx="11" cy="11" r="9" fill="none" stroke="#1d2f52" stroke-width="2"/><path d="M6.5 11.5l3 3 6-6" fill="none" stroke="#1d2f52" stroke-width="2"/></svg><span>One two-hour visit where your child will complete an MRI scan, answer questions</span></li>
      <li><svg width="22" height="22" viewBox="0 0 22 22"><circle cx="11" cy="11" r="9" fill="none" stroke="#1d2f52" stroke-width="2"/><path d="M6.5 11.5l3 3 6-6" fill="none" stroke="#1d2f52" stroke-width="2"/></svg><span>about their puberty stage, and have a small hair sample taken to study puberty hormones</span></li>
    </ul>
  </section>

  <section class="eligibility">
    <h2>Your child may be<br>eligible if they</h2>
    <div class="criterion">
      <svg width="56" height="44" viewBox="0 0 56 44" fill="#e99b15"><circle cx="12" cy="14" r="5"/><rect x="6" y="21" width="12" height="20" rx="3"/><circle cx="28" cy="10" r="6"/><rect x="21" y="18" width="14" height="24" rx="3"/><circle cx="44" cy="6" r="6"/><rect x="37" y="14" width="14" height="28" rx="3"/></svg>
      <span>Are age 10-17</span>
    </div>
    <div class="criterion">
      <svg width="56" height="50" viewBox="0 0 56 50" fill="#e99b15"><path d="M14 16c0-8 6-13 14-13s13 6 13 13c0 5-3 8-4 11v10h-8v8H14V30c-2-4 0-8 0-14z"/><circle cx="46" cy="10" r="7"/><circle cx="8" cy="8" r="6"/><rect x="40" y="24" width="14" height="10" rx="5"/></svg>
      <span>Tend to worry or overthink negative thoughts</span>
    </div>
    <div class="criterion">
      <svg width="56" height="54" viewBox="0 0 56 54"><rect x="4" y="4" width="30" height="40" rx="2" fill="none" stroke="#e99b15" stroke-width="3"/><path d="M10 14h18M10 22h14M10 30h10" stroke="#e99b15" stroke-width="3"/><circle cx="36" cy="34" r="9" fill="#fff" stroke="#e99b15" stroke-width="3"/><path d="M43 41l8 8" stroke="#e99b15" stroke-width="4"/></svg>
      <span>have not been diagnosed with psychosis, learning problems, or autism</span>
    </div>
  </section>

  <p class="cta">Interested in participating? Want more information?<br>Please contact us!</p>

  <svg class="footer-band" viewBox="0 0 1200 170" preserveAspectRatio="none"><path d="M0 100 C 250 40, 700 -10, 1200 20 L1200 170 L0 170 Z" fill="#172d4f"/></svg>
  <div class="email">molvtstudy@halvern.edu</div>
  <div class="study-name">MOLVT</div>
</main>
</body>
</html>
```